Business Cards for a Junk Removal Company

Hello,
We are looking to have business cards designed that are simple, bold, easy to read, and right to the point. Please see the attachments for our logo files. We want the card to be yellow on both sides ( Color code Yellow: #FFE01B). The logo text font is (Rockstar Extra Bold) and this is also in the files attached. Please make the text black for the logo. On the back side of the card, you can use white and black for text. Thank you in advance for your hard work!

Front of card-
Harbor Haul Removal (logo)
Back of card-
Harbor Haul Removal
Donate - Recycle - Dispose
518-276-9053
www.harborhaulremoval.example
info@harborhaulremoval.example

Industry/Entity Type

Junk removal

Contact Information for Business Card

FRONT OF CARD- Harbor Haul Removal (logo) BACK OF CARD- Harbor Haul Removal Donate - Recycle - Dispose 518-276-9053 www.harborhaulremoval.example info@harborhaulremoval.example

Font styles to use
Other font styles liked:
• Rockstar Extra Bold

Colors
FFF300
FFF600
FEFA6F
FFFEC7
FFFEE8

Requirements
Must have
• Must have color code Yellow: #FFE01B for the background of front and back of the card

```html
<!DOCTYPE html>
<html lang="en">
<head>
<meta charset="utf-8">
<title>Harbor Haul Removal – Business Cards</title>
<link rel="stylesheet" href="https://fonts.googleapis.com/css2?family=Anton&family=Poppins:wght@500&display=swap">
<style>
  :root {
    --yellow: #FFE01B;
    --yellow-deep: #FFD60A;
    --dark: #1c1505;
    --dark-soft: #2a1f0a;
    --navy: #0f1833;
    --white: #ffffff;
    --stage: #a6a6a6;
  }
  * { margin: 0; padding: 0; box-sizing: border-box; }
  html, body { width: 848px; height: 1200px; overflow: hidden; }
  body { background: var(--stage); position: relative; font-family: "Anton", sans-serif; }

  .card {
    position: absolute; left: 164px; width: 520px; height: 297px;
    overflow: hidden; box-shadow: 3px 4px 6px rgba(0,0,0,.35);
  }
  .card--contact { top: 286px; }
  .card--brand { top: 616px; }

  .photo-yellow {
    position: absolute; inset: 0;
    background: linear-gradient(120deg, var(--yellow) 0%, var(--yellow-deep) 55%, var(--yellow) 100%);
  }
  .photo-dark {
    position: absolute; left: 0; top: 0; width: 100%; height: 151px;
    background: linear-gradient(100deg, var(--dark) 0%, var(--dark-soft) 60%, var(--dark) 100%);
  }

  .logo-word {
    position: absolute; color: var(--white); text-transform: uppercase;
    font-family: "Anton", sans-serif; line-height: 1; text-align: center;
  }
  .card--contact .logo-word { left: 30px; top: 40px; width: 132px; font-size: 23px; }
  .card--contact .logo-word span { display: block; font-size: 12px; letter-spacing: 3px; margin-top: 4px; }

  .divider { position: absolute; left: 168px; top: 39px; width: 1.5px; height: 48px; background: var(--yellow); }

  .contact-line {
    position: absolute; left: 186px; display: flex; align-items: center; gap: 8px;
    color: var(--white); font-family: "Poppins", sans-serif; font-weight: 500; font-size: 15.5px; line-height: 1;
  }
  .contact-line svg { width: 14px; height: 14px; flex: none; }
  .contact-line--phone { top: 42px; font-size: 17px; }
  .contact-line--mail { top: 66px; }

  .service { position: absolute; top: 116px; width: 130px; margin-left: -65px; text-align: center; }
  .service-badge {
    width: 66px; height: 66px; margin: 0 auto; border-radius: 50%;
    background: #0b0b0b; border: 4px solid var(--white);
    display: flex; align-items: center; justify-content: center;
  }
  .service-badge svg { width: 34px; height: 34px; }
  .service-name { margin-top: 3px; font-size: 27px; color: var(--navy); line-height: 1.1; letter-spacing: .5px; }
  .service--donate { left: 98px; }
  .service--recycle { left: 253px; }
  .service--dispose { left: 419px; }

  .rule { position: absolute; left: 244px; top: 234px; width: 31px; height: 2px; background: var(--white); }

  .web {
    position: absolute; left: 0; width: 100%; text-align: center;
    font-size: 15px; letter-spacing: 4.6px; line-height: 1; text-transform: uppercase;
  }
  .card--contact .web { top: 252px; color: #111; }

  .card--brand .logo-word {
    left: 0; width: 100%; top: 88px; color: #0b0b0b; font-size: 52px;
  }
  .card--brand .logo-word span { display: block; font-size: 22px; letter-spacing: 7px; margin-top: 6px; }
  .footer-band { position: absolute; left: 0; bottom: 0; width: 100%; height: 62px; background: var(--dark); }
  .card--brand .web { bottom: 23px; color: var(--white); }
</style>
</head>
<body>

<section class="card card--contact">
  <div class="photo-yellow" role="img" aria-label="Yellow-tinted photo of junk bags being hauled"></div>
  <div class="photo-dark" role="img" aria-label="Dark-tinted photo of workers carrying junk"></div>

  <div class="logo-word">Harbor Haul<span>Removal</span></div>
  <div class="divider"></div>

  <div class="contact-line contact-line--phone">
    <svg viewBox="0 0 24 24"><path fill="#FFE01B" d="M6.6 10.8a15 15 0 0 0 6.6 6.6l2.2-2.2c.3-.3.7-.4 1-.2 1.1.4 2.3.6 3.6.6.6 0 1 .4 1 1V20c0 .6-.4 1-1 1A17 17 0 0 1 3 4c0-.6.4-1 1-1h3.5c.6 0 1 .4 1 1 0 1.3.2 2.5.6 3.6.1.3 0 .7-.2 1z"/></svg>
    518-276-9053
  </div>
  <div class="contact-line contact-line--mail">
    <svg viewBox="0 0 24 24"><rect x="2" y="5" width="20" height="14" fill="none" stroke="#FFE01B" stroke-width="2"/><path d="M2 5l10 8 10-8" fill="none" stroke="#FFE01B" stroke-width="2"/></svg>
    info@harborhaulremoval.example
  </div>

  <div class="service service--donate">
    <div class="service-badge">
      <svg viewBox="0 0 24 24"><path fill="#FFE01B" d="M12 12s-6-3.6-6-7.2C6 3 7.3 2 8.7 2c1.3 0 2.3.8 3.3 2 1-1.2 2-2 3.3-2C16.7 2 18 3 18 4.8 18 8.4 12 12 12 12z"/><rect x="3" y="14" width="3" height="7" fill="#FFE01B"/><path fill="#FFE01B" d="M7 14h6c1 0 1.6.7 1.6 1.5H10v1h6l4-2c1-.4 2 .8 1.2 1.6L16 21H7z"/></svg>
    </div>
    <div class="service-name">DONATE</div>
  </div>

  <div class="service service--recycle">
    <div class="service-badge">
      <svg viewBox="0 0 24 24" fill="#FFE01B"><path d="M9.5 3h5l2.5 4.3 1.7-1-1.6 5-5-1 1.7-1L12 5.8 9.6 9.9 6.9 8.4z"/><path d="M20.5 13l2.3 4.1-2.4 4H15v2l-3.5-3.7L15 15.6v2h3.8l-2-3.5z"/><path d="M4 12.6l2.7 1.5-2.1 3.5H9V21H3.7l-2.4-4.1 2.5-4.3L2 11.6l5-1.4.9 5z"/></svg>
    </div>
    <div class="service-name">RECYCLE</div>
  </div>

  <div class="service service--dispose">
    <div class="service-badge">
      <svg viewBox="0 0 24 24" fill="#FFE01B"><circle cx="15" cy="3.5" r="2.2"/><path d="M12.5 7h5l1.5 14h-2.5l-1.5-7-2 7H11l1.5-7z"/><path d="M4 11h7l-1 10H5z" fill="none" stroke="#FFE01B" stroke-width="1.6"/></svg>
    </div>
    <div class="service-name">DISPOSE</div>
  </div>

  <div class="rule"></div>
  <div class="web">www.harborhaulremoval.example</div>
</section>

<section class="card card--brand">
  <div class="photo-yellow" role="img" aria-label="Yellow-tinted photo of a worker lifting junk bags"></div>
  <div class="logo-word">Harbor Haul<span>Removal</span></div>
  <div class="footer-band"></div>
  <div class="web">www.harborhaulremoval.example</div>
</section>

</body>
</html>
```